Create our new Velora Coffee Syrup Label designs. A delicious job!

Design a front label for a range of coffee syrup flavours. The brand is 'Velora Coffee Syrups'. The flavours, vanilla, hazelnut and caramel.
Our coffee syrups are made with only natural colours and flavours and are positioned in the popular premium space in Australian and international cafes.
The labels will be applied to 750 ml Boston Bottles (see attached image).
Given that coffee syrups are often positioned in high visibility locations in cafes, they can be considered as objects of functional beauty.
This range is a sub brand for our company and I have attached our main brand images in the flavours we want. we want this brand to look different to this Tarnwick branded range, but included the image to show what we are currently doing in this space.
The different flavours can be identified by a combination of colour and text, which may be a line or section of the otherwise same overall design.
We are going to do a 2 part label with the front just carrying Brand and flavour descriptors plus 750 ml.
Total Bottle height is 240 mm bottle width is 70 mm

Target Market(s)

Cafe patrons, primarily women, 18-35, Middle class in terms of economics, regular cafe patrons. Who are looking for a guilt free treat in their busy day.

Logo Text

Velora Coffee Syrups Vanilla (or Hazelnut, or Caramel) 750 ml

Logo styles of interest
Pictorial/Combination Logo
Font styles to use
Sans Serif

Colors

Designer to choose colors to be used in the design.

Requirements
Must have
• A clear design, which is a combination of font and image. it needs to be legible from up to 2m away (across a counter in a cafe).
• We would like to see a device, which may be a gold drop, that may be the 'velora' meant to the coffee.
• The way our coffee syrups are used is by adding a small amount (15 ml) to a cup
• of coffee, this adds both flavour and sweetness to the overall coffee experience, and cafes charge a premium for this service. We want our package to show this will be a great thing to do.
• We have a few options in terms of Label stock. We can print on a foil, that will allow a metallic sheen to come through the colours (see example of the Tarnwick branded bottles.
Nice to have
• We are looking for a modern, clean and distinctive look and feel to this range.
• I have added a key line for the front and back label, however we can create a different label die line should the design warrant that. Note this is just for the front label.
Should not have
• Difficult to read fonts or imagery that is not clear.
• Should look different to the Tarnwick branded product range.

```html
<!DOCTYPE html>
<html lang="en">
<head>
<meta charset="utf-8">
<title>Velora Coffee Syrups – Front Labels</title>
<link rel="stylesheet" href="https://fonts.googleapis.com/css2?family=Open+Sans:wght@800&family=Source+Sans+3:ital,wght@0,300;1,300&display=swap">
<style>
  :root {
    --page: #ffffff;
    --label-edge: #c9c9c9;
    --white: #ffffff;
    --ink: #1d1d1d;
    --caramel: #ef922c;
    --caramel-accent: #e4534c;
    --hazelnut: #4a35d8;
    --hazelnut-accent: #72d6c9;
    --vanilla: #ec4f4b;
    --vanilla-accent: #b4dc5e;
  }
  * { box-sizing: border-box; margin: 0; padding: 0; }
  html, body {
    width: 1200px; height: 848px; overflow: hidden;
    background: var(--page);
  }
  .sheet {
    position: relative; width: 1200px; height: 848px;
  }
  .label-row {
    position: absolute; top: 60px; left: 60px;
    display: flex; gap: 45px;
  }
  .label {
    width: 330px; height: 512px;
    background: var(--white);
    border: 1.5px solid var(--label-edge);
    border-radius: 18px;
    padding: 7px;
  }
  .label__panel {
    position: relative; width: 100%; height: 100%;
    border-radius: 12px; overflow: hidden;
    background: var(--flavour);
  }
  .label--caramel  { --flavour: var(--caramel);  --accent: var(--caramel-accent); }
  .label--hazelnut { --flavour: var(--hazelnut); --accent: var(--hazelnut-accent); }
  .label--vanilla  { --flavour: var(--vanilla);  --accent: var(--vanilla-accent); }

  .vertical {
    position: absolute; top: 34px;
    writing-mode: vertical-rl;
    transform: rotate(180deg);
    white-space: nowrap;
    line-height: 1;
  }
  .label__flavour {
    left: 44px;
    font-family: "Open Sans", sans-serif;
    font-weight: 800; font-size: 68px;
    letter-spacing: 4px;
    color: var(--white);
  }
  .label__brand {
    font-family: "Source Sans 3", sans-serif;
    font-weight: 300; font-size: 30px;
    letter-spacing: 1px;
    color: var(--accent);
  }
  .label__brand--line1 { left: 118px; }
  .label__brand--line2 { left: 164px; }

  .label__photo {
    position: absolute; left: 134px; top: 300px;
    width: 410px; height: 410px;
    border-radius: 50%;
    border: 6px solid var(--white);
  }
  .label--caramel .label__photo {
    background: radial-gradient(circle at 30% 30%, #f3c077, #c97a1f 55%, #8a4c12);
  }
  .label--hazelnut .label__photo {
    background: radial-gradient(circle at 30% 30%, #b98558, #8a5530 55%, #5e3519);
  }
  .label--vanilla .label__photo {
    background: radial-gradient(circle at 30% 30%, #9c6a45, #5a3a2a 50%, #3b3633);
  }

  .label__volume {
    position: absolute; left: 2px; bottom: -8px;
    font-family: "Source Sans 3", sans-serif;
    font-style: italic; font-weight: 300;
    font-size: 46px; line-height: 1;
    color: var(--white);
  }

  .sheet__note {
    position: absolute; left: 720px; top: 610px;
    font-family: "Source Sans 3", sans-serif;
    font-style: italic; font-weight: 300;
    font-size: 34px; line-height: 1.2;
    color: var(--ink);
  }
  .sheet__note span { display: block; }
  .sheet__note .indent { padding-left: 14px; }
</style>
</head>
<body>
<main class="sheet">
  <div class="label-row">
    <article class="label label--caramel">
      <div class="label__panel">
        <h2 class="vertical label__flavour">CARAMEL</h2>
        <p class="vertical label__brand label__brand--line1">VELORA COFFEE</p>
        <p class="vertical label__brand label__brand--line2">• SYRUPS</p>
        <div class="label__photo" role="img" aria-label="Close-up photo of glossy caramel sauce pouring"></div>
        <p class="label__volume">750ml</p>
      </div>
    </article>

    <article class="label label--hazelnut">
      <div class="label__panel">
        <h2 class="vertical label__flavour">HAZELNUT</h2>
        <p class="vertical label__brand label__brand--line1">VELORA COFFEE</p>
        <p class="vertical label__brand label__brand--line2">• SYRUPS</p>
        <div class="label__photo" role="img" aria-label="Photo of a pile of whole hazelnuts"></div>
        <p class="label__volume">750ml</p>
      </div>
    </article>

    <article class="label label--vanilla">
      <div class="label__panel">
        <h2 class="vertical label__flavour">VANILLA</h2>
        <p class="vertical label__brand label__brand--line1">VELORA COFFEE</p>
        <p class="vertical label__brand label__brand--line2">• SYRUPS</p>
        <div class="label__photo" role="img" aria-label="Photo of vanilla pods and cinnamon sticks on a dark surface"></div>
        <p class="label__volume">750ml</p>
      </div>
    </article>
  </div>

  <p class="sheet__note">
    <span>*Pic just for sample</span>
    <span class="indent">not real include</span>
    <span>- clean and</span>
    <span class="indent">distinctive look</span>
  </p>
</main>
</body>
</html>
```